Building Servicess

We need a new business card design for a company. We specialise in: Electrical/Site temporary electrics, Data/Network Installation, Passive Fire Protection

Industry/Entity Type

Construction

Contact Information for Business Card

Services provided as detailed on project description

Font styles to use
Serif

Colors
0054AA
0677BA
7BADD7
CADEEF
E8F1F8
00AB8E
00BBA5
67D7C9
C6EFE9
E9F9F6
EB3D1F
EC4F4E
F09395
F8D3D4
FCEDEE

Requirements
Must have
• Company logo-contact details-phone numbers

```html
<!DOCTYPE html>
<html lang="en">
<head>
<meta charset="utf-8">
<title>Norvale Building Services – Business Card</title>
<link rel="stylesheet" href="https://fonts.googleapis.com/css2?family=Montserrat:wght@400;500;700;800&display=swap">
<style>
  :root {
    --stage: #9a9a9c;
    --paper: #ffffff;
    --brand-blue: #0054AA;
    --brand-mid: #0677BA;
    --brand-light: #7BADD7;
    --ink-grey: #6d6e71;
    --ink-dark: #3a3b3d;
    --rule: #c9cacc;
    --white: #ffffff;
  }
  * { box-sizing: border-box; margin: 0; padding: 0; }
  html, body { width: 1200px; height: 800px; overflow: hidden; }
  body {
    background: var(--stage);
    font-family: "Montserrat", Arial, sans-serif;
    position: relative;
  }
  .card {
    position: absolute;
    top: 245px;
    width: 540px;
    height: 310px;
    box-shadow: 0 10px 24px rgba(0,0,0,0.25);
  }
  /* Front */
  .card-front {
    left: 40px;
    background: var(--paper);
    display: flex;
    align-items: center;
  }
  .brand {
    width: 260px;
    display: flex;
    align-items: center;
    justify-content: center;
    gap: 10px;
    padding-left: 20px;
  }
  .brand-square {
    width: 22px; height: 22px;
    background: var(--brand-blue);
    flex: none;
  }
  .brand-name {
    color: var(--brand-blue);
    font-weight: 700;
    font-size: 17px;
    line-height: 1.25;
    letter-spacing: 0.5px;
    text-transform: uppercase;
  }
  .divider {
    width: 1px;
    height: 170px;
    background: var(--rule);
  }
  .contact {
    padding-left: 28px;
  }
  .person-name {
    color: var(--brand-blue);
    font-weight: 800;
    font-size: 20px;
    letter-spacing: 0.5px;
    text-transform: uppercase;
  }
  .person-title {
    color: var(--ink-grey);
    font-size: 12px;
    margin-top: 2px;
    margin-bottom: 16px;
  }
  .contact-list { list-style: none; }
  .contact-item {
    display: flex;
    align-items: center;
    gap: 9px;
    color: var(--ink-dark);
    font-size: 12px;
    line-height: 20px;
  }
  .contact-icon { width: 12px; height: 12px; flex: none; }
  /* Back */
  .card-back {
    left: 620px;
    background: linear-gradient(135deg, var(--brand-mid) 0%, var(--brand-blue) 100%);
    color: var(--white);
    display: flex;
    flex-direction: column;
    align-items: center;
    justify-content: center;
    text-align: center;
  }
  .back-brand {
    display: flex;
    align-items: center;
    gap: 12px;
    margin-bottom: 34px;
  }
  .back-brand .brand-square { background: #28c8f5; width: 26px; height: 26px; }
  .back-brand-name {
    font-weight: 700;
    font-size: 24px;
    letter-spacing: 1px;
    text-transform: uppercase;
    color: var(--white);
  }
  .specialise-heading {
    font-weight: 800;
    font-size: 17px;
    letter-spacing: 0.5px;
    margin-bottom: 6px;
  }
  .services {
    font-size: 12px;
    line-height: 18px;
    font-weight: 500;
  }
</style>
</head>
<body>

<section class="card card-front">
  <div class="brand">
    <span class="brand-square"></span>
    <span class="brand-name">Norvale Building<br>Services Ltd</span>
  </div>
  <div class="divider"></div>
  <div class="contact">
    <div class="person-name">Daniel Hartley</div>
    <div class="person-title">President</div>
    <ul class="contact-list">
      <li class="contact-item">
        <svg class="contact-icon" viewBox="0 0 12 12"><path d="M2.5 1 L4.5 1 L5 3.5 L3.8 4.4 Q4.8 6.8 7.6 8.2 L8.5 7 L11 7.5 L11 9.5 Q10.5 11 8.8 11 Q1 9.5 1 2.8 Q1 1 2.5 1 Z" fill="var(--brand-blue)"/></svg>
        555-014-2763
      </li>
      <li class="contact-item">
        <svg class="contact-icon" viewBox="0 0 12 12"><rect x="3" y="0.8" width="6" height="10.4" rx="1" fill="none" stroke="var(--brand-blue)" stroke-width="1.4"/><circle cx="6" cy="9.3" r="0.7" fill="var(--brand-blue)"/></svg>
        555-018-4419
      </li>
      <li class="contact-item">
        <svg class="contact-icon" viewBox="0 0 12 12"><rect x="0.5" y="2" width="11" height="8" rx="1" fill="var(--brand-blue)"/><path d="M1 2.6 L6 6.5 L11 2.6" fill="none" stroke="#fff" stroke-width="1"/></svg>
        info@norvalebuilding.com
      </li>
      <li class="contact-item">
        <svg class="contact-icon" viewBox="0 0 12 12"><circle cx="6" cy="6" r="5.2" fill="var(--brand-blue)"/><path d="M0.8 6 H11.2 M6 0.8 Q3 6 6 11.2 M6 0.8 Q9 6 6 11.2" fill="none" stroke="#fff" stroke-width="0.8"/></svg>
        www.norvalebuilding.com
      </li>
    </ul>
  </div>
</section>

<section class="card card-back">
  <div class="back-brand">
    <span class="brand-square"></span>
    <span class="back-brand-name">Norvale</span>
  </div>
  <div class="specialise-heading">WE SPECIALISE IN</div>
  <p class="services">Electrical/Site temporary electrics Data/Network Installation<br>Passive Fire Protection</p>
</section>

</body>
</html>
```